Lanternfield Billboard - Financial Services Company (Investments, Tax Planning and Insurance)

Our new office has a billboard directly above the office building. We'd like something eye-catching with a strong Call to Action, with the main part of the billboard being under 7 words if possible. We'd like you to include a way to get ahold of us (either our website lanternfieldllc.example or our phone number 302-418-2967. You may also include in small font something to indicate that we've been serving the area Since 1987 (The Harbor County Area, The Three-River Region, the Copperleaf Basin, etc.)

We offer financial planning, tax planning, and insurance, and we help our clients to focus on their goals and happiness by providing everything they need for lifelong wealth under one roof.

Our logos are attached, we use a triangle logo with green and gray. We use the tagline "Steady Plans For Every Stage" but this does not need to be included.

Potential ideas we have seen from other financial companies-
- the concept that the driver spends more time looking at billboards than planning for their retirement
-something along the lines of "everything you need for your finances is in this building right here" planning, investments, taxes, insurance"
-don't spend your time worrying about retirement, let us help you plan for it
-are you working for your money, or is it working for you?
- retirement takes planning, we're here to help
- ready to retire? talk to us
- need investment advice?
- need help investing?
- crossing your fingers isn't a retirement plan. we can help.
- retiring soon? you need help.

Those are just general ideas, please feel free to be creative.

brand colors:
#00b585
#00b185
#000000
#ffffff
#6d6f75
#6d6f75
#6f7074
#021712
#052e24

```html
<!DOCTYPE html>
<html lang="en">
<head>
<meta charset="utf-8">
<title>Lanternfield Billboard</title>
<link rel="stylesheet" href="https://fonts.googleapis.com/css2?family=Questrial&family=Hind:wght@500;600;700&display=swap">
<style>
  :root {
    --green: #00a862;
    --gray: #6d6f75;
    --stage: #58585a;
    --white: #ffffff;
    --photo-light: #e9e6df;
    --photo-mid: #b7bcc6;
    --photo-dark: #4f5d7a;
  }
  html, body {
    margin: 0;
    width: 1200px;
    height: 1200px;
    overflow: hidden;
    background: var(--stage);
  }
  .stage {
    width: 1200px;
    height: 1200px;
    display: flex;
    align-items: center;
    justify-content: center;
  }
  .billboard {
    width: 1120px;
    height: 560px;
    display: block;
  }
  .headline {
    font-family: "Questrial", sans-serif;
    font-size: 80px;
    fill: var(--gray);
  }
  .headline .accent { fill: var(--green); }
  .cta {
    font-family: "Hind", sans-serif;
    font-weight: 700;
    font-size: 88px;
    fill: var(--white);
  }
  .brand-name {
    font-family: "Hind", sans-serif;
    font-weight: 600;
    font-size: 82px;
    fill: var(--green);
  }
  .brand-tagline {
    font-family: "Questrial", sans-serif;
    font-size: 17px;
    letter-spacing: 5px;
    fill: var(--gray);
  }
  .phone {
    font-family: "Hind", sans-serif;
    font-weight: 700;
    font-size: 86px;
    fill: var(--gray);
  }
  .web {
    font-family: "Hind", sans-serif;
    font-weight: 500;
    font-size: 42px;
    letter-spacing: 2px;
    fill: var(--gray);
  }
  .web .domain { fill: var(--green); }
  .since {
    font-family: "Hind", sans-serif;
    font-weight: 600;
    font-size: 19px;
    fill: var(--white);
  }
</style>
</head>
<body>
<main class="stage">
  <svg class="billboard" viewBox="0 0 1450 725" xmlns="http://www.w3.org/2000/svg" aria-label="Lanternfield retirement planning billboard">
    <defs>
      <linearGradient id="panel-fade" x1="0" y1="0" x2="1" y2="1">
        <stop offset="0" stop-color="#ececec"/>
        <stop offset="0.55" stop-color="#ffffff"/>
      </linearGradient>
      <linearGradient id="photo-tone" x1="0" y1="0" x2="1" y2="1">
        <stop offset="0" stop-color="var(--photo-light)"/>
        <stop offset="0.45" stop-color="var(--photo-mid)"/>
        <stop offset="1" stop-color="var(--photo-dark)"/>
      </linearGradient>
    </defs>

    <rect class="panel" width="1450" height="725" fill="url(#panel-fade)"/>

    <polygon class="accent-band" fill="var(--green)"
             points="1110,0 1138,0 818,531 0,531 0,328 916,328"/>

    <g role="img" aria-label="Photo of a smiling senior couple embracing outdoors">
      <polygon class="photo-area" fill="url(#photo-tone)"
               points="1158,0 1186,0 1450,452 1450,531 840,531"/>
    </g>

    <polygon class="gray-stripe" fill="var(--gray)"
             points="1196,0 1226,0 1450,388 1450,440"/>

    <text class="headline">
      <tspan x="68" y="128">DON'T SPEND YOUR</tspan>
      <tspan x="68" y="204">TIME WORRYING</tspan>
      <tspan x="68" y="280">ABOUT <tspan class="accent">RETIREMENT</tspan></tspan>
    </text>

    <text class="cta">
      <tspan x="64" y="422">LET US HELP</tspan>
      <tspan x="64" y="504">YOU PLAN FOR IT</tspan>
    </text>

    <g class="brand">
      <rect x="68" y="572" width="40" height="40" fill="var(--gray)"/>
      <text class="brand-name" x="122" y="626">Lanternfield</text>
      <text class="brand-tagline" x="124" y="658">STEADY PLANS FOR EVERY STAGE</text>
    </g>

    <g class="contact">
      <g class="phone-icon" transform="translate(800,560)" fill="var(--green)">
        <path d="M10 4 C4 8 2 18 8 30 C14 42 24 52 34 54 C40 55 44 52 46 48 L38 40 C36 38 33 38 31 40 L28 43 C22 40 16 32 14 26 L18 23 C20 21 20 18 19 16 L14 4 C13 2 11 2 10 4 Z"/>
        <path d="M30 8 a18 18 0 0 1 16 16" fill="none" stroke="var(--green)" stroke-width="4" stroke-linecap="round"/>
        <path d="M30 17 a9 9 0 0 1 8 8" fill="none" stroke="var(--green)" stroke-width="4" stroke-linecap="round"/>
      </g>
      <text class="phone" x="1355" y="616" text-anchor="end">302-418-2967</text>
      <text class="web" x="1355" y="668" text-anchor="end">www.<tspan class="domain">lanternfieldllc</tspan>.example</text>
    </g>

    <rect class="since-bar" x="0" y="683" width="1450" height="42" fill="var(--gray)"/>
    <text class="since" x="725" y="711" text-anchor="middle">SERVING THE AREA SINCE 1987 (THE HARBOR COUNTY AREA, THE THREE-RIVER REGION, THE COPPERLEAF BASIN, ETC.)</text>
  </svg>
</main>
</body>
</html>
```